Harbor Quill is a Smart Device and Wiring Business offering the latest in Smart Home Devices inc

Looking for a new website to draw people to my business and explain what a smart home is all about. I currently own a domain and have a website I put together in webnimbus business website builder. address www.harborquill.com. The website needs modernising and be visually appealing with cool action buttons, client feedback page etc.

The webpage needs to present an image of seamless integration of wireless voice control and smart devices that take tasks and activities away from the owner saving them time and money.

I have a chatterbay business page(harbor quill) and snapmeadow linked with the business, are we able to link this to the website somehow?

Target Market(s)

Residential home owners who want to modernise their home. Who have seen adverts for orbit nook and kestrel nova and want to put it in their home.

Industry/Entity Type

Technology Equipment

Number of Pages Required

1 page

Colors

Designer to choose colors to be used in the design.

Requirements
Must have
• A great landing page, that is modern and attractive, that gets across the idea of smart devices and technology.
• Must be ios/android device friendly.
Nice to have
• interactive/animated buttons
• I like the direction and interactiveness of these websites, a simplified version would be awesome.
• Something in between:
• http://www.oakridgelofts.com/ and https://plumcove.com/
• http://www.oakridgelofts.com/

```html
<!DOCTYPE html>
<html lang="en">
<head>
<meta charset="utf-8">
<title>Harbor Quill — Smart Device Integration</title>
<link href="https://fonts.googleapis.com/css2?family=Jost:wght@400;500;600;700&display=swap" rel="stylesheet">
<style>
:root{
  --blue:#1f8dc6;
  --blue-dark:#177aae;
  --navy:#1b2640;
  --navy-deep:#151e33;
  --bar:#3b404b;
  --bar-dark:#2f333c;
  --ink:#1b2640;
  --text:#4a4f5a;
  --muted:#8a8f98;
  --white:#ffffff;
  --field:#e4e7ec;
}
*{box-sizing:border-box;margin:0;padding:0}
html,body{width:1200px;height:3435px;overflow:hidden}
body{font-family:"Jost",sans-serif;color:var(--text);background:var(--white);position:relative}
.section{position:absolute;left:0;width:1200px;overflow:hidden}
.abs{position:absolute}
.btn{position:absolute;display:flex;align-items:center;justify-content:center;font-size:13px;font-weight:500;letter-spacing:.3px}
.btn-solid{background:var(--blue);color:var(--white)}
.btn-outline{border:2px solid var(--white);color:var(--white)}
.btn-outline-blue{border:2px solid var(--blue);color:var(--blue);background:var(--white)}
.center{left:0;width:1200px;text-align:center}
.eyebrow{font-size:13px;color:var(--ink)}
.h2{font-size:36px;font-weight:600;color:var(--ink)}
.h2 span{color:var(--blue)}

/* header */
.site-header{top:0;height:87px;background:var(--white);box-shadow:0 1px 4px rgba(0,0,0,.08);z-index:2}
.brand{left:80px;top:24px;display:flex;align-items:center;gap:12px}
.brand-dot{width:36px;height:36px;border-radius:50%;background:var(--blue)}
.brand-name{font-size:24px;font-weight:700;color:var(--navy)}
.nav{top:34px;font-size:14px;color:var(--ink)}
.nav.active{color:var(--blue);text-decoration:underline}

/* hero */
.hero{top:87px;height:440px}
.hero-photo{position:absolute;inset:0;background:linear-gradient(120deg,#d9d9d9 0%,#a9a9a9 45%,#5e5e5e 75%,#c4c4c4 100%)}
.hero-title{top:133px;font-size:38px;font-weight:600;color:var(--white)}
.hero-sub{top:182px;font-size:21px;line-height:29px;color:var(--white)}

/* about */
.about{top:527px;height:496px}
.about-panel{left:0;top:0;width:751px;height:496px;background:var(--blue)}
.about-photo{left:751px;top:0;width:449px;height:496px;background:linear-gradient(160deg,#4a3a2e,#1c1814 70%)}
.about .eyebrow{color:var(--navy)}
.about-title{left:156px;top:88px;font-size:36px;font-weight:600;color:var(--navy)}
.about-title span{color:var(--white);font-weight:500}
.about-h{left:156px;font-size:17px;font-weight:600;color:var(--navy)}
.about-p{left:156px;width:520px;font-size:13px;line-height:19px;color:var(--white)}

/* services */
.services{top:1023px;height:569px}
.card{top:161px;width:280px;height:277px;overflow:hidden}
.card-label{position:absolute;left:24px;bottom:24px;font-size:16px;color:var(--white)}
.card-feature{background:var(--navy-deep)}
.card-feature h3{position:absolute;left:24px;top:118px;font-size:16px;font-weight:500;color:var(--white)}
.card-feature p{position:absolute;left:24px;top:150px;width:230px;font-size:13px;line-height:19px;color:#d6dbe4}
.card-feature .more{position:absolute;left:24px;top:232px;font-size:13px;color:var(--blue);text-decoration:underline}
.arrow{font-size:26px;color:var(--ink)}

/* CTA bands */
.cta-blue{top:1592px;height:160px;background:var(--blue)}
.cta-dark{top:2210px;height:160px;background:var(--navy)}
.cta-small{left:231px;top:48px;font-size:20px;font-weight:600;color:var(--white)}
.cta-big{left:231px;top:80px;font-size:32px;color:var(--white)}

/* process */
.process{top:1752px;height:458px}
.step-title{font-size:17px;color:var(--ink);text-align:center;width:260px}
.step-text{font-size:13px;line-height:19px;color:var(--text);text-align:center;width:260px}

/* testimonial */
.testimonial{top:2370px;height:470px}
.quote-mark{font-size:70px;color:var(--blue);font-weight:700;line-height:1}
.quote-text{top:225px;left:320px;width:560px;font-size:17px;line-height:24px;color:var(--muted);text-align:center}

/* footer */
.quote-footer{top:2840px;height:515px;background:var(--navy)}
.quote-footer .eyebrow{color:var(--white)}
.quote-footer .h2{color:var(--white)}
.field{position:absolute;background:var(--field);font-size:11px;color:var(--muted);padding:8px 10px}
.contact-line{top:470px;font-size:14px;color:var(--white);font-weight:500;display:flex;gap:16px;align-items:center;justify-content:center}
.contact-line a{color:var(--blue);font-weight:400}
.social{display:flex;gap:10px;align-items:center}
.social span{display:flex;align-items:center;gap:5px;font-size:12px;font-weight:400}
.social i{width:12px;height:12px;border-radius:50%;background:var(--white);display:inline-block}
.bottom-bar{top:3355px;height:80px;background:var(--bar)}
.copyright{left:156px;top:30px;font-size:13px;color:#c9ccd2}
.copyright a{color:var(--blue);text-decoration:underline}
.to-top{left:1000px;top:0;width:200px;height:80px;background:var(--bar-dark)}
</style>
</head>
<body>

<header class="section site-header">
  <div class="abs brand"><span class="brand-dot"></span><span class="brand-name">Harbor Quill</span></div>
  <span class="abs nav active" style="left:380px">Home</span>
  <span class="abs nav" style="left:455px">About Us</span>
  <span class="abs nav" style="left:550px">What We Do</span>
  <span class="abs nav" style="left:666px">Products</span>
  <span class="abs nav" style="left:756px">Testimonials</span>
  <span class="abs nav" style="left:868px">Contact Us</span>
  <a class="btn btn-solid" style="left:968px;top:27px;width:152px;height:35px">Request a Demo</a>
</header>

<section class="section hero">
  <div class="hero-photo" role="img" aria-label="Modern living room with wall-mounted television and smart home devices"></div>
  <h1 class="abs center hero-title">Smart Device Integration</h1>
  <p class="abs center hero-sub">We are focused on delivering affordable and easily usable<br>devices for your home and office!</p>
  <a class="btn btn-outline-blue" style="left:536px;top:268px;width:128px;height:35px;border:none">Explore More</a>
</section>

<section class="section about">
  <div class="abs about-panel"></div>
  <div class="abs about-photo" role="img" aria-label="Hand holding a phone app that unlocks a smart door lock"></div>
  <span class="abs eyebrow" style="left:156px;top:60px">Welcome to</span>
  <h2 class="abs about-title">Harbor <span>Quill</span></h2>
  <h3 class="abs about-h" style="top:148px">Our Aim</h3>
  <p class="abs about-p" style="top:184px">Our aim is to bring affordable smart home products to everyone, offering seamless integration and reliability. With a wide range of available cost options, outstanding service and experience, we are the solution for all your smart home technology solutions...</p>
  <h3 class="abs about-h" style="top:264px">Our Story</h3>
  <p class="abs about-p" style="top:302px">Harbor Quill began as an idea in a garage and a belief that home technology should be readily available and reasonably priced. We are constantly sourcing and experimenting with new technologies and solutions to create any vision of the future you can imagine ...</p>
  <a class="btn btn-outline" style="left:156px;top:398px;width:128px;height:35px">Explore More</a>
</section>

<section class="section services">
  <span class="abs center eyebrow" style="top:69px">Our Speciality</span>
  <h2 class="abs center h2" style="top:98px">What <span>We Do</span></h2>
  <span class="abs arrow" style="left:118px;top:282px">&#8249;</span>
  <span class="abs arrow" style="left:1066px;top:282px">&#8250;</span>
  <div class="abs card" style="left:156px;background:linear-gradient(160deg,#e8eef3,#9fb0bf)" role="img" aria-label="Wall-mounted home automation touch panel">
    <span class="card-label">Home Automation</span>
  </div>
  <div class="abs card card-feature" style="left:460px">
    <h3>Home Theatre Design</h3>
    <p>Looking to create a cinematic experience in your home? Learn the basics, including how to set goals ...</p>
    <span class="more">Read More &rarr;</span>
  </div>
  <div class="abs card" style="left:763px;background:linear-gradient(160deg,#5f7ea2,#1f3452)" role="img" aria-label="Viewer watching an action film on a large screen">
    <span class="card-label">Media Entertainment</span>
  </div>
  <a class="btn btn-outline-blue" style="left:543px;top:472px;width:114px;height:33px">View All</a>
</section>

<section class="section cta-blue">
  <svg class="abs" style="left:0;top:0" width="1200" height="160" aria-hidden="true">
    <polygon points="0,0 50,0 0,50" fill="#fff"/>
    <polygon points="1200,110 1200,160 1150,160" fill="#fff"/>
  </svg>
  <span class="abs cta-small">Harbor Quill</span>
  <span class="abs cta-big">Smart Home turn you on?</span>
  <a class="btn btn-outline" style="left:815px;top:61px;width:151px;height:37px">Request a Demo</a>
</section>

<section class="section process">
  <span class="abs center eyebrow" style="top:71px">Install &amp; Setup</span>
  <h2 class="abs center h2" style="top:100px">The <span>Process</span></h2>
  <svg class="abs" style="left:0;top:0" width="1200" height="458" aria-hidden="true">
    <g fill="none" stroke="#8fc3e0" stroke-width="2" stroke-dasharray="4 6">
      <line x1="240" y1="325" x2="420" y2="222"/>
      <line x1="512" y1="222" x2="690" y2="330"/>
      <line x1="775" y1="330" x2="955" y2="222"/>
    </g>
    <line x1="465" y1="256" x2="465" y2="290" stroke="#1f8dc6" stroke-width="2"/>
    <line x1="728" y1="296" x2="728" y2="262" stroke="#1f8dc6" stroke-width="2"/>
    <circle cx="197" cy="343" r="40" fill="#fff" stroke="#e3e8ee" stroke-width="2"/>
    <g fill="#1f8dc6"><circle cx="190" cy="336" r="6"/><circle cx="204" cy="339" r="5"/><rect x="181" y="345" width="18" height="10" rx="5"/><rect x="199" y="347" width="13" height="8" rx="4"/></g>
    <circle cx="465" cy="211" r="45" fill="#fff" stroke="#e3e8ee" stroke-width="2"/>
    <g stroke="#1f8dc6" stroke-width="4" stroke-linecap="round"><line x1="452" y1="198" x2="478" y2="224"/><line x1="478" y1="198" x2="452" y2="224"/></g>
    <circle cx="728" cy="339" r="45" fill="#fff" stroke="#1f8dc6" stroke-width="3"/>
    <circle cx="728" cy="339" r="16" fill="#1f8dc6"/>
    <polyline points="720,339 726,345 737,333" fill="none" stroke="#fff" stroke-width="3"/>
    <circle cx="998" cy="211" r="40" fill="#fff" stroke="#e3e8ee" stroke-width="2"/>
    <circle cx="998" cy="211" r="15" fill="none" stroke="#1f8dc6" stroke-width="4"/>
    <circle cx="998" cy="211" r="6" fill="none" stroke="#1f8dc6" stroke-width="3"/>
  </svg>
  <h3 class="abs step-title" style="left:67px;top:160px">Consultation</h3>
  <p class="abs step-text" style="left:67px;top:184px">We meet to discuss your vision, gather requirements, and properly scope out your project timeline and pricing ...</p>
  <h3 class="abs step-title" style="left:351px;top:297px">Installation</h3>
  <p class="abs step-text" style="left:351px;top:321px">Upon acceptance of project document we build your system in our workshop testing every element for operability ...</p>
  <h3 class="abs step-title" style="left:603px;top:160px">Finalisation</h3>
  <p class="abs step-text" style="left:603px;top:184px">After installing the product we run you through your system, making sure you are happy with the final product and functionability ...</p>
  <h3 class="abs step-title" style="left:870px;top:297px">Support</h3>
  <p class="abs step-text" style="left:870px;top:321px">We offer tech support when difficulties arise, making sure that your product continues to deliver as advertised ...</p>
</section>

<section class="section cta-dark">
  <svg class="abs" style="left:0;top:0" width="1200" height="160" aria-hidden="true">
    <polygon points="0,0 50,0 0,50" fill="#1f8dc6"/>
    <polygon points="1200,110 1200,160 1150,160" fill="#1f8dc6"/>
  </svg>
  <span class="abs cta-small">We Are Ready</span>
  <span class="abs cta-big">To get your project started</span>
  <a class="btn btn-solid" style="left:838px;top:62px;width:128px;height:34px">Contact Us</a>
</section>

<section class="section testimonial">
  <span class="abs center eyebrow" style="top:71px">Testimonial</span>
  <h2 class="abs center h2" style="top:100px">What Our <span>Clients Say</span></h2>
  <span class="abs center quote-mark" style="top:160px">&ldquo;</span>
  <p class="abs quote-text">There are many variations of passages of Lorem Ipsum which available, but the majority have suffered alteration in some form, by injected humour, or randomised words which don't look even slightly believable. If you are going to use a passage of Lorem...</p>
  <span class="abs center quote-mark" style="top:325px">&rdquo;</span>
  <span class="abs" style="left:460px;top:392px;font-size:18px;color:var(--ink)">&larr;</span>
  <span class="abs center" style="top:392px;font-size:15px;color:var(--ink)">-- Standard Chunk --</span>
  <span class="abs" style="left:722px;top:392px;font-size:18px;color:var(--ink)">&rarr;</span>
</section>

<section class="section quote-footer">
  <span class="abs center eyebrow" style="top:77px">Send Message</span>
  <h2 class="abs center h2" style="top:106px">Get a <span>Free Quote</span></h2>
  <div class="field" style="left:309px;top:183px;width:282px;height:32px">Name:</div>
  <div class="field" style="left:607px;top:183px;width:284px;height:32px">Phone:</div>
  <div class="field" style="left:309px;top:233px;width:282px;height:32px">Email:</div>
  <div class="field" style="left:607px;top:233px;width:284px;height:32px">Subject <span style="float:right">&#9662;</span></div>
  <div class="field" style="left:309px;top:284px;width:582px;height:77px">Message:</div>
  <a class="btn btn-solid" style="left:543px;top:377px;width:114px;height:35px">Submit</a>
  <div class="abs" style="left:309px;top:442px;width:582px;height:1px;background:#3a4660"></div>
  <div class="abs center contact-line">
    <span>Phone: <a>123-456-7890</a></span><span>|</span>
    <span>Email: <a>info@harborquill.com</a></span>
    <span style="margin-left:20px">Get Social:</span>
    <span class="social"><span><i></i>Chatterbay</span><span><i></i>Flitwire</span><span><i></i>Snapmeadow</span></span>
  </div>
</section>

<footer class="section bottom-bar">
  <p class="abs copyright">&copy; 2018 <a>Harbor Quill</a>. All right reserved. &nbsp; | &nbsp; <a>Privacy Policy</a></p>
  <div class="abs to-top">
    <svg class="abs" style="left:92px;top:32px" width="16" height="16" aria-hidden="true">
      <polyline points="3,8 8,3 13,8" fill="none" stroke="#fff" stroke-width="2"/>
      <polyline points="3,13 8,8 13,13" fill="none" stroke="#fff" stroke-width="2"/>
    </svg>
  </div>
</footer>

</body>
</html>
```